Direct Mail flyer for the timeshare industry.

We need someone who has experience in direct mail experience in postcards and successful campaigns. The post card we are using is not good at all.

We are looking at a 5.5 x 8.5 postcard with 4 color on one side and the black and white on the mailing side. But if someone has a better idea instead of a postcard then I am open to that

Target Market(s)

Timeshare owners...most of them are 55 plus in age. We help people get out of their time share

Industry/Entity Type

Industry

Font styles to use
Serif

Colors

Designer to choose colors to be used in the design.

Requirements
Must have
• Call to action and be easy to understand and look very professional and not fake or cheesy

```html
<!DOCTYPE html>
<html lang="en">
<head>
<meta charset="utf-8">
<title>Private Event Invitation Postcard</title>
<link href="https://fonts.googleapis.com/css2?family=Jost:wght@400;500;600;700&family=Oswald:wght@500;600&display=swap" rel="stylesheet">
<style>
  :root {
    --page: #ece9e4;
    --header-grey: #e6e6e6;
    --red: #e3262b;
    --red-band: #d9262b;
    --green: #4cae47;
    --green-band: #45a843;
    --navy: #1f2433;
    --space-dark: #05070d;
    --white: #ffffff;
    --ink: #141414;
  }
  * { box-sizing: border-box; margin: 0; padding: 0; }
  html, body { width: 1200px; height: 1200px; overflow: hidden; }
  body { background: var(--page); font-family: "Jost", sans-serif; position: relative; }

  .postcard { position: absolute; left: 211px; width: 779px; height: 504px; box-shadow: 0 6px 14px rgba(0,0,0,.28); overflow: hidden; }
  .postcard--front { top: 74px; background: var(--space-dark); }
  .postcard--back { top: 624px; background: var(--white); }

  .headline-band { position: absolute; left: 0; top: 0; width: 100%; height: 66px; background: linear-gradient(#f0f0f0, var(--header-grey)); display: flex; align-items: center; justify-content: center; }
  .headline-band h1 { color: var(--red); font-weight: 700; font-size: 29px; letter-spacing: .4px; text-transform: uppercase; }

  .starfield { position: absolute; left: 0; top: 66px; width: 100%; height: 356px;
    background: radial-gradient(ellipse 30% 22% at 82% 54%, rgba(60,170,80,.55), transparent 70%),
                radial-gradient(ellipse 60% 35% at 50% 62%, rgba(30,70,110,.55), transparent 75%),
                var(--space-dark); }

  .rule { position: absolute; left: 130px; width: 519px; height: 1.5px; background: #d8d8d8; }
  .chance { position: absolute; left: 0; width: 100%; top: 88px; text-align: center; color: var(--red); font-size: 44px; font-weight: 500; letter-spacing: .5px; }
  .invite-line { position: absolute; left: 0; width: 100%; top: 146px; text-align: center; color: var(--white); font-size: 21px; line-height: 27px; font-weight: 400; }
  .invite-line strong { color: var(--green); font-family: "Oswald", sans-serif; font-weight: 500; }

  .benefits { position: absolute; left: 0; top: 262px; width: 100%; height: 160px; background: rgba(31,36,51,.93); }
  .benefit { position: absolute; top: 0; width: 240px; text-align: center; }
  .benefit__icon { position: absolute; left: 95px; top: -17px; width: 50px; height: 50px; border-radius: 50%; border: 2px solid var(--green); background: #142016; display: flex; align-items: center; justify-content: center; }
  .benefit__title { margin-top: 41px; color: var(--green); font-size: 20px; font-weight: 500; letter-spacing: .3px; }
  .benefit__text { margin-top: 4px; color: var(--white); font-size: 12.5px; line-height: 16.6px; }
  .divider { position: absolute; top: 20px; width: 1px; height: 130px; background: var(--green); opacity: .6; }

  .details-bar { position: absolute; left: 0; top: 422px; width: 100%; height: 82px; display: flex; }
  .venue-tag { width: 33px; background: var(--white); display: flex; align-items: center; justify-content: center; }
  .venue-tag span { transform: rotate(-90deg); color: var(--red); font-size: 14px; white-space: nowrap; }
  .event-info { width: 406px; background: var(--red-band); display: flex; align-items: center; color: var(--white); }
  .event-info__venue { width: 154px; text-align: center; font-size: 13.5px; line-height: 15.5px; font-weight: 500; }
  .event-info__sep { width: 1px; height: 62px; background: rgba(255,255,255,.7); }
  .event-info__date { flex: 1; text-align: center; font-size: 16px; line-height: 20px; }
  .rsvp { flex: 1; background: var(--green-band); color: var(--white); text-align: center; padding-top: 4px; }
  .rsvp__call { font-family: "Oswald", sans-serif; font-size: 23px; font-weight: 500; line-height: 30px; }
  .rsvp__code { margin: 4px auto 0; width: 218px; height: 24px; border: 1px solid var(--white); font-size: 15px; line-height: 22px; }
  .rsvp__note { font-family: "Oswald", sans-serif; font-size: 10px; font-weight: 500; margin-top: 3px; }

  .return-address { position: absolute; left: 38px; top: 28px; color: var(--ink); font-size: 16px; line-height: 20px; font-weight: 500; }
  .stamp-box { position: absolute; left: 662px; top: 31px; width: 96px; height: 88px; border: 1px solid var(--ink); }
</style>
</head>
<body>

<section class="postcard postcard--front">
  <header class="headline-band"><h1>A Private Event Invitation - Limited Seating</h1></header>
  <div class="starfield" role="img" aria-label="Starry night sky with a soft green glow"></div>

  <div class="rule" style="top:83px"></div>
  <h2 class="chance">THIS IS YOUR CHANCE!</h2>
  <div class="rule" style="top:141px"></div>
  <p class="invite-line">We’ve arranged for you andone guest to<br>attend our Harbor Point Group Event <strong>FREE of charge.</strong></p>

  <div class="benefits">
    <div class="benefit" style="left:29px">
      <div class="benefit__icon">
        <svg width="26" height="22" viewBox="0 0 26 22"><path d="M13 2 25 8 13 14 1 8Z" fill="#fff"/><path d="M6 11v5c2 3 12 3 14 0v-5l-7 3.5Z" fill="#fff"/><path d="M23 9v7" stroke="#fff" stroke-width="1.5"/></svg>
      </div>
      <h3 class="benefit__title">EDUCATION</h3>
      <p class="benefit__text">Promise this event will be<br>an eye-opening experience and<br>an incredible learning<br>opportunity regardless of your<br>current situation.</p>
    </div>
    <div class="divider" style="left:275px"></div>
    <div class="benefit" style="left:276px">
      <div class="benefit__icon">
        <svg width="20" height="24" viewBox="0 0 20 24"><path d="M10 1 19 4v7c0 6-4 10-9 12C5 21 1 17 1 11V4Z" fill="#fff"/><path d="M6 12l3 3 5-6" fill="none" stroke="#142016" stroke-width="2"/></svg>
      </div>
      <h3 class="benefit__title">PROTECTION</h3>
      <p class="benefit__text">Arm yourself with the<br>knowledge of how to avoid<br>the current scams occurring in<br>the timeshare industry to<br>protect you as an owner.</p>
    </div>
    <div class="divider" style="left:517px"></div>
    <div class="benefit" style="left:517px">
      <div class="benefit__icon">
        <svg width="26" height="22" viewBox="0 0 26 22"><rect x="1" y="2" width="14" height="10" rx="2" fill="#fff"/><path d="M4 12v4l4-4Z" fill="#fff"/><rect x="11" y="8" width="14" height="9" rx="2" fill="#fff" stroke="#142016" stroke-width="1.2"/><path d="M22 17v4l-4-4Z" fill="#fff"/></svg>
      </div>
      <h3 class="benefit__title">ADVISEMENT</h3>
      <p class="benefit__text">Your questions are welcomed<br>and will be addressed. This<br>will bring you the sense of<br>confidence that you have<br>been seeking.</p>
    </div>
  </div>

  <div class="details-bar">
    <div class="venue-tag"><span>Our Venue</span></div>
    <div class="event-info">
      <p class="event-info__venue">Lakeside Garden Hotel<br>2150 Meadow Parkway<br>Ardenville, TX 75012</p>
      <div class="event-info__sep"></div>
      <p class="event-info__date">Saturday, February 17, 2018<br>10:30 AM | 3:00 PM | 6:00 PM</p>
    </div>
    <div class="rsvp">
      <p class="rsvp__call">CALL (888) 555-0142 TODAY WITH</p>
      <p class="rsvp__code">RSVP Code # HPG70218</p>
      <p class="rsvp__note">TO GUARANTEE YOUR SEATS!</p>
    </div>
  </div>
</section>

<section class="postcard postcard--back">
  <address class="return-address" style="font-style:normal">Harbor Point Group, LLC<br>720 W Orchard Bend Lane<br>Millbrook, Mo. 65800</address>
  <div class="stamp-box"></div>
</section>

</body>
</html>
```